FREE Network Assessment image for landing page

This graphic will be on a landing page and on the left will be Text and a download button that we change and control. The graphic for this project will be to the right.
I will add an example of the landing page area so that it makes more sense.

Please include the text from the sample - the font needs to be the same style as what we are using on the left side!

The graphic needs to be a .png file, roughly 713 x 527 white background. Use discretion on design layout.

Colors are black, Red = PMS 1795 and Gray = Cool Gray 10

Thanks,
Tom Harwick

Target Market(s)

small businesses

Industry/Entity Type

Information Technology

Font styles to use
Other font styles liked:
• See sample

Requirements
Must have
• see description
Nice to have
• Possibly small technology related image to help enhance the text but I don't want any image to compete with the text. Keep in mind the colors mentioned in the description - this is the web site colors.
Should not have
• Should not be hard to read

```html
<!DOCTYPE html>
<html lang="en">
<head>
<meta charset="utf-8">
<title>Free Network &amp; Computer Health Check Service</title>
<link href="https://fonts.googleapis.com/css2?family=Oswald:wght@400&family=Lato:wght@400;700&display=swap" rel="stylesheet">
<style>
  :root {
    --paper: #ffffff;
    --ink: #3f3f42;
    --red: #c9504f;
    --red-bright: #f04a4d;
    --icon-black: #1c1c1c;
    --icon-red: #e3262b;
    --photo-top: #e6edf4;
    --photo-bottom: #c9d4df;
  }
  html, body {
    margin: 0;
    padding: 0;
    width: 1200px;
    height: 888px;
    overflow: hidden;
    background: var(--paper);
  }
  .health-check {
    position: relative;
    width: 1200px;
    height: 888px;
    background: var(--paper);
  }
  .headline {
    position: absolute;
    left: 56px;
    top: 38px;
    margin: 0;
    font-family: "Oswald", "Arial Narrow", sans-serif;
    font-weight: 400;
    font-size: 80px;
    line-height: 84px;
    color: var(--ink);
    letter-spacing: -0.5px;
  }
  .benefit-list {
    list-style: none;
    margin: 0;
    padding: 0;
  }
  .benefit {
    position: absolute;
    left: 56px;
    width: 700px;
    display: flex;
    align-items: flex-start;
  }
  .benefit-icon {
    width: 58px;
    height: 58px;
    flex: none;
    margin-right: 22px;
    margin-top: 0;
  }
  .benefit-text {
    font-family: "Lato", Arial, sans-serif;
    font-size: 28px;
    line-height: 34px;
    color: var(--red);
  }
  .cta-button {
    position: absolute;
    left: 57px;
    top: 760px;
    width: 469px;
    height: 78px;
    border-radius: 39px;
    background: var(--red-bright);
    color: var(--paper);
    font-family: "Oswald", "Arial Narrow", sans-serif;
    font-size: 34px;
    line-height: 78px;
    text-align: center;
    text-decoration: none;
  }
  .presenter-photo {
    position: absolute;
    left: 790px;
    top: 262px;
    width: 410px;
    height: 626px;
    background: linear-gradient(180deg, var(--photo-top), var(--photo-bottom));
    border-radius: 200px 200px 0 0;
  }
</style>
</head>
<body>
<main class="health-check">
  <h1 class="headline">FREE NETWORK &amp;<br>COMPUTER HEALTH CHECK SERVICE</h1>

  <ul class="benefit-list">
    <li class="benefit" style="top:276px">
      <svg class="benefit-icon" viewBox="0 0 40 40" aria-hidden="true">
        <circle cx="16" cy="16" r="12" fill="none" stroke="var(--icon-black)" stroke-width="3"/>
        <line x1="25" y1="25" x2="36" y2="36" stroke="#888" stroke-width="5" stroke-linecap="round"/>
        <ellipse cx="16" cy="17" rx="4" ry="5.5" fill="var(--icon-red)"/>
        <circle cx="16" cy="10.5" r="2.5" fill="var(--icon-red)"/>
      </svg>
      <span class="benefit-text">Check your network’s security against hacker attacks, theft, ransomware, viruses, and more.</span>
    </li>
    <li class="benefit" style="top:380px">
      <svg class="benefit-icon" viewBox="0 0 40 40" aria-hidden="true">
        <rect x="3" y="4" width="34" height="32" rx="2" fill="#fff" stroke="#bbb" stroke-width="1.5"/>
        <rect x="3" y="4" width="34" height="5" fill="var(--icon-black)"/>
        <circle cx="20" cy="23" r="8" fill="var(--icon-red)" stroke="var(--icon-black)" stroke-width="2"/>
        <circle cx="20" cy="23" r="2.5" fill="var(--icon-black)"/>
      </svg>
      <span class="benefit-text">See who and what has access to your network and data.</span>
    </li>
    <li class="benefit" style="top:482px">
      <svg class="benefit-icon" viewBox="0 0 40 40" aria-hidden="true">
        <rect x="3" y="4" width="34" height="32" rx="2" fill="#fff" stroke="#bbb" stroke-width="1.5"/>
        <rect x="3" y="4" width="34" height="5" fill="var(--icon-black)"/>
        <path d="M9 30 A11 11 0 0 1 31 30 Z" fill="var(--icon-red)"/>
        <line x1="20" y1="30" x2="20" y2="19" stroke="#fff" stroke-width="2"/>
      </svg>
      <span class="benefit-text">Perform network and Internet speed test</span>
    </li>
    <li class="benefit" style="top:552px">
      <svg class="benefit-icon" viewBox="0 0 40 40" aria-hidden="true">
        <rect x="3" y="5" width="34" height="24" rx="2" fill="#fff" stroke="var(--icon-black)" stroke-width="3"/>
        <rect x="16" y="29" width="8" height="5" fill="var(--icon-black)"/>
        <rect x="11" y="34" width="18" height="2.5" fill="var(--icon-black)"/>
        <circle cx="20" cy="17" r="7" fill="var(--icon-red)"/>
        <rect x="16" y="15" width="8" height="4" fill="#fff"/>
      </svg>
      <span class="benefit-text">Resolve PC slowness issues, security vulnerabilities and improper configurations</span>
    </li>
    <li class="benefit" style="top:659px">
      <svg class="benefit-icon" viewBox="0 0 40 40" aria-hidden="true">
        <rect x="3" y="5" width="34" height="24" rx="2" fill="var(--icon-red)" stroke="var(--icon-black)" stroke-width="2"/>
        <rect x="16" y="29" width="8" height="5" fill="var(--icon-black)"/>
        <rect x="11" y="34" width="18" height="2.5" fill="var(--icon-black)"/>
        <circle cx="12" cy="15" r="4.5" fill="#fff"/>
        <rect x="21" y="18" width="3" height="7" fill="#fff"/>
        <rect x="26" y="14" width="3" height="11" fill="#fff"/>
        <rect x="31" y="10" width="3" height="15" fill="#fff"/>
      </svg>
      <span class="benefit-text">Validate your backups are working and recoverable in a timely fashion.</span>
    </li>
  </ul>

  <a class="cta-button" href="#book">BOOK AN APPOINTMENT NOW!</a>

  <div class="presenter-photo" role="img" aria-label="Photo of a smiling IT technician sitting cross-legged with a laptop, gesturing toward the list"></div>
</main>
</body>
</html>
```